TrellisCover Mobile App needs a new skin

We need to add some sparkle to our mobile application. The app is already built with some of the functionality, screens and components (vanilla material design) and now it needs some styling and inspiration. The application simplifies insurance form capturing and communication to/from the broker. Further to that it has some value added services.

Industry/Entity Type

Insurance Broker

Font styles to use
Sans Serif

Requirements
Must have
• Modern, friendly styling and colors. Material design principles.
Nice to have
• Thinking of a themed background photo with the form elements in a more glassy / semi transparent style.
• Would like to use the same app for some customers as a white labeled version, then just change the themed background image, logo and select dark or light theme for them.

```html
<!DOCTYPE html>
<html lang="en">
<head>
<meta charset="utf-8">
<title>TrellisCover – Sign up</title>
<link rel="stylesheet" href="https://fonts.googleapis.com/css2?family=Quicksand:wght@300;400;500;700&display=swap">
<style>
  :root {
    --page: #ffffff;
    --screen: #4a9a6b;
    --field: #3e845b;
    --field-edge: #5aa77a;
    --rule: #5fae80;
    --icon-dark: #2f6c48;
    --ink: #ffffff;
  }
  * { box-sizing: border-box; margin: 0; padding: 0; }
  html, body { width: 771px; height: 1200px; overflow: hidden; background: var(--page); }
  body { position: relative; font-family: "Quicksand", sans-serif; color: var(--ink); }

  .app-screen {
    position: absolute; left: 101px; top: 161px; width: 569px; height: 896px;
    background: var(--screen); overflow: hidden;
  }

  .status-bar { position: absolute; left: 0; top: 14px; width: 100%; height: 34px; }
  .status-bar .mail { position: absolute; left: 14px; top: 6px; }
  .status-bar .clock {
    position: absolute; left: 0; width: 100%; text-align: center; top: 4px;
    font-size: 17px; font-weight: 700;
  }
  .status-bar .indicators { position: absolute; right: 10px; top: 4px; display: flex; align-items: center; gap: 8px; font-size: 15px; font-weight: 700; }

  .brand { position: absolute; top: 122px; width: 100%; text-align: center; font-size: 50px; letter-spacing: 1px; }
  .brand .light { font-weight: 300; }
  .brand .bold { font-weight: 700; }
  .pager { position: absolute; top: 200px; width: 100%; display: flex; justify-content: center; gap: 3px; }
  .pager span { width: 8px; height: 8px; border-radius: 50%; background: var(--ink); }
  .pager span.off { background: transparent; border: 1.5px solid var(--ink); }

  .signup-form { position: absolute; left: 0; top: 328px; width: 100%; }
  .field-row { position: relative; height: 99px; }
  .field-row::after {
    content: ""; position: absolute; left: 70px; right: 60px; top: 82px; height: 2px;
    background: var(--rule); opacity: .6;
  }
  .field-icon { position: absolute; left: 14px; top: 12px; width: 36px; height: 40px; }
  .field-box {
    position: absolute; left: 63px; width: 438px; height: 62px; top: 0;
    background: var(--field); border: 1.5px solid var(--field-edge); border-radius: 16px;
    padding-left: 14px; display: flex; align-items: center;
    font-size: 37px; font-style: italic; font-weight: 300; letter-spacing: -.3px;
  }

  .tab-bar { position: absolute; left: 0; top: 750px; width: 100%; height: 146px; display: flex; }
  .tab { position: relative; flex: 1 1 0; min-width: 0; text-align: center; }
  .tab + .tab::before {
    content: ""; position: absolute; left: 0; top: 0; width: 1.5px; height: 100px; background: var(--icon-dark); opacity: .5;
  }
  .tab svg { display: block; margin: 4px auto 0; width: 100px; height: 92px; }
  .tab .label {
    position: absolute; left: 0; right: 0; bottom: 14px; display: block;
    text-align: center; font-size: 25px; font-weight: 500; letter-spacing: .5px;
  }
</style>
</head>
<body>
<main class="app-screen">
  <div class="status-bar">
    <svg class="mail" width="36" height="22" viewBox="0 0 36 22"><rect width="36" height="22" rx="2" fill="#fff"/><path d="M1 1 L18 13 L35 1" fill="none" stroke="var(--screen)" stroke-width="2.5"/></svg>
    <div class="clock">14:54</div>
    <div class="indicators">
      <svg width="14" height="20" viewBox="0 0 14 20"><path d="M7 19 C3 13 1 10 1 7 a6 6 0 0 1 12 0 c0 3-2 6-6 12z" fill="none" stroke="#fff" stroke-width="2"/><circle cx="7" cy="7" r="2" fill="#fff"/></svg>
      <svg width="24" height="18" viewBox="0 0 24 18"><path d="M2 6 a14 14 0 0 1 20 0 M5.5 9.5 a9 9 0 0 1 13 0 M9 13 a4 4 0 0 1 6 0" fill="none" stroke="#fff" stroke-width="2.5"/><circle cx="12" cy="16" r="1.8" fill="#fff"/></svg>
      <svg width="12" height="20" viewBox="0 0 12 20"><path d="M1 6 L10 14 L6 18 V2 L10 6 L1 14" fill="none" stroke="#fff" stroke-width="1.8"/></svg>
      <span>21%</span>
      <svg width="48" height="20" viewBox="0 0 48 20"><rect x="1" y="1" width="42" height="18" rx="4" fill="none" stroke="#fff" stroke-width="2"/><rect x="4" y="4" width="9" height="12" rx="1" fill="#fff"/><rect x="44" y="6" width="3" height="8" rx="1" fill="#fff"/></svg>
    </div>
  </div>

  <h1 class="brand"><span class="light">TRELLIS</span> <span class="bold">COVER</span></h1>
  <div class="pager"><span></span><span></span><span class="off"></span><span class="off"></span></div>

  <form class="signup-form">
    <div class="field-row">
      <svg class="field-icon" viewBox="0 0 36 40"><circle cx="18" cy="13" r="9" fill="#fff"/><path d="M2 38 c0-12 8-15 16-15 s16 3 16 15z" fill="#fff"/></svg>
      <div class="field-box">NAME</div>
    </div>
    <div class="field-row">
      <svg class="field-icon" viewBox="0 0 36 40"><path d="M10 18 V12 a8 8 0 0 1 16 0 V18" fill="none" stroke="#fff" stroke-width="3.5"/><rect x="6" y="17" width="24" height="21" rx="4" fill="#fff"/></svg>
      <div class="field-box">PASSWORD</div>
    </div>
    <div class="field-row">
      <svg class="field-icon" viewBox="0 0 36 40"><rect x="8" y="2" width="20" height="36" rx="5" fill="none" stroke="#fff" stroke-width="3"/><line x1="12" y1="31" x2="24" y2="31" stroke="#fff" stroke-width="2"/></svg>
      <div class="field-box">PHONE NUMBER</div>
    </div>
    <div class="field-row">
      <svg class="field-icon" viewBox="0 0 36 40"><path d="M18 38 C10 27 6 21 6 14 a12 12 0 0 1 24 0 c0 7-4 13-12 24z" fill="#fff"/><circle cx="18" cy="14" r="5" fill="var(--screen)"/></svg>
      <div class="field-box">LOCATION</div>
    </div>
  </form>

  <nav class="tab-bar">
    <div class="tab">
      <svg viewBox="0 0 100 92"><path d="M50 8 L88 44 H78 V86 H58 V62 H42 V86 H22 V44 H12z" fill="var(--icon-dark)"/></svg>
      <span class="label">HOME</span>
    </div>
    <div class="tab">
      <svg viewBox="0 0 100 92"><path d="M50 6 C62 14 74 16 84 16 C84 52 72 74 50 88 C28 74 16 52 16 16 C26 16 38 14 50 6z" fill="var(--icon-dark)"/><path d="M34 48 L46 60 L68 36" fill="none" stroke="var(--screen)" stroke-width="4"/></svg>
      <span class="label">INSURE</span>
    </div>
    <div class="tab">
      <svg viewBox="0 0 100 92"><rect x="10" y="30" width="80" height="32" rx="14" fill="var(--icon-dark)" transform="rotate(45 50 46)"/><rect x="10" y="30" width="80" height="32" rx="14" fill="var(--icon-dark)" transform="rotate(-45 50 46)"/><g fill="var(--screen)"><circle cx="42" cy="46" r="3"/><circle cx="58" cy="46" r="3"/><circle cx="50" cy="38" r="3"/><circle cx="50" cy="54" r="3"/></g></svg>
      <span class="label">CLAIM</span>
    </div>
    <div class="tab">
      <svg viewBox="0 0 100 92"><circle cx="50" cy="32" r="18" fill="var(--icon-dark)"/><path d="M14 88 c0-24 16-34 36-34 s36 10 36 34z" fill="var(--icon-dark)"/></svg>
      <span class="label">PROFILE</span>
    </div>
  </nav>
</main>
</body>
</html>
```